Unique Home Cooking School needs Wordpress Design

We need a wordpress design for our small business based in Singapore called Brisk Ladles. It is a unique cooking school where the cooking course menu is completely customised to our client's preference/lifestyle/requests. More information can be found on our site: briskladles.example

We are looking for something simple and easy to navigate. We are currently using a free template which we have customised ourselves. As the business is growing, we are looking to have a site more suited to our needs. The site should also be photo friendly, as we often post up photos of our food. It should also be social media integrated as a lot of our business is driven by PQ.

The look and feel should really reflect the personalities of both owners - like the logo. Please feel free to contact us if you need more clarification.

Target Market(s)

Our target audience are usually female, with children, aged 25 - 45.
They are either stay-at-home mums or full-time mums that are keen to do more for the family.

Industry/Entity Type

Small Business

Requirements
Must have
• The wordpress design has to be able to accommodate food photos on every page.
It also needs to be able to support social media feeds within the site.
Should not have
• Design should not have any chef-like design elements as we are not chefs. We are two stay-home-mums wanting to impart skills to other stay-home-mums or domestic helpers.

```html
<!DOCTYPE html>
<html lang="en">
<head>
<meta charset="utf-8">
<title>Brisk Ladles Cooking School</title>
<link href="https://fonts.googleapis.com/css2?family=PT+Sans:wght@400;700&display=swap" rel="stylesheet">
<style>
:root{
  --red:#c8101e;
  --red-head:#d0021b;
  --pink:#f7899a;
  --blue-soft:#9cc8dc;
  --ink:#1a1a1a;
  --body:#555;
  --muted:#7a7a7a;
  --paper:#faf6f5;
  --paper-deep:#f3eceb;
  --footer:#1f1f1f;
  --frame:#e4e0e0;
}
*{margin:0;padding:0;box-sizing:border-box}
html,body{width:896px;height:1200px;overflow:hidden}
body{position:relative;font-family:"PT Sans",Arial,sans-serif;color:var(--ink);background:var(--paper)}
.abs{position:absolute}

.topline{left:0;top:0;width:896px;height:5px;background:#000}
.header{left:0;top:5px;width:896px;height:87px;background:#fff}
.brand{left:104px;top:14px;width:110px;height:70px;text-align:center}
.brand-dot{display:block;width:34px;height:34px;border-radius:50%;background:var(--pink);margin:0 auto 4px}
.brand-name{font-size:13px;color:#333;font-weight:400;line-height:14px}
.brand-tag{font-size:5.5px;color:#555;line-height:8px}
.contact{right:100px;top:19px;font-size:10px;color:#111}
.contact .sms{color:var(--pink)}
.contact .tel{color:var(--blue-soft)}
.nav{top:53px;right:95px;display:flex;gap:0}
.nav a{display:block;font-size:13.5px;color:#111;text-decoration:none;padding:0 9px;line-height:22px;letter-spacing:.3px}
.nav a.current{background:#000;color:#fff}

.hero{left:0;top:92px;width:896px;height:325px;background:radial-gradient(ellipse at 50% 60%,#f6d36a 0%,#f1a25a 30%,#e9b98f 55%,#f4e6d6 80%,#e8d0b8 100%)}
.hero-title{left:0;top:232px;width:896px;text-align:center;font-size:20px;letter-spacing:.5px;color:#2a2a2a}
.hero-text{left:0;top:262px;width:896px;text-align:center;font-size:12px;line-height:21px;color:#2a2a2a}
.arrow{top:236px;width:48px;height:48px}

.welcome-title{left:0;top:455px;width:896px;text-align:center;font-size:18px;font-weight:700;color:var(--red-head);letter-spacing:.6px}
.welcome-text{left:128px;top:493px;width:640px;text-align:center;font-size:11.6px;line-height:16.8px;color:#333}
.btn{display:block;background:var(--red);color:#fff;font-size:10px;letter-spacing:.4px;text-align:center;line-height:22px;height:22px;border-radius:3px;text-decoration:none}
.welcome-btn{left:407px;top:578px;width:79px}

.band{left:0;top:616px;width:896px;height:304px;background:#fff}
.col{top:628px;width:186px}
.col h2{font-size:20px;font-weight:400;letter-spacing:.4px;color:var(--ink);line-height:24px}
.col h2 span{color:var(--pink)}
.col .shot{margin-top:6px;width:186px;height:121px;border:3px solid var(--frame)}
.col p{margin-top:10px;font-size:8.6px;line-height:12.7px;color:var(--muted);text-align:justify}
.col .btn{position:absolute;top:260px;right:0;width:80px}

.section-h{font-size:20px;font-weight:400;letter-spacing:.4px;color:var(--ink)}
.section-h span{color:var(--pink)}
.blog{left:115px;top:978px;width:320px}
.blog ul{margin-top:13px;list-style:none}
.blog li{font-size:9.3px;line-height:21px;color:#333;position:relative;padding-left:26px}
.blog li::before{content:"";position:absolute;left:2px;top:9px;width:3px;height:3px;border-radius:50%;background:#333}
.testi{left:467px;top:978px;width:307px}
.testi p{margin-top:13px;font-size:9.3px;line-height:21px;color:#333;text-align:justify}
.quote{color:var(--pink);font-size:18px;font-weight:700;line-height:0;vertical-align:-3px}
.testi .who{text-align:right;font-size:9.3px;color:#333;margin-top:3px}

.stripe-pink{left:0;top:1145px;width:450px;height:9px;background:var(--pink)}
.stripe-blue{left:450px;top:1145px;width:446px;height:9px;background:var(--blue-soft)}
.footer{left:0;top:1154px;width:896px;height:46px;background:var(--footer)}
.copy{left:120px;top:1165px;font-size:10px;color:var(--pink)}
.slogan{right:100px;top:1165px;font-size:9.5px;color:var(--blue-soft)}
.social{right:100px;top:1180px;display:flex;gap:6px;font-size:9.5px;color:#fff}
.social a{color:#fff;text-decoration:none}
</style>
</head>
<body>
<div class="abs topline"></div>
<header class="abs header"></header>

<div class="abs brand">
  <span class="brand-dot"></span>
  <div class="brand-name">Brisk Ladles</div>
  <div class="brand-tag">Cooking Lessons for Everyone</div>
</div>
<div class="abs contact">Email us: info@briskladles.example&nbsp; <span class="sms">SMS / ChatLine / Call Us :</span> <span class="tel">+65.8000.1234 / +65.9000.5678</span></div>
<nav class="abs nav">
  <a class="current" href="#">HOME</a>
  <a href="#">ABOUT US</a>
  <a href="#">COURSES</a>
  <a href="#">BLOG</a>
  <a href="#">CONTACT US</a>
</nav>

<section class="abs hero" role="img" aria-label="Close-up photo of pastry tartlets filled with diced peppers and salmon, garnished with herbs"></section>
<div class="abs hero-title">CONVENIENT, FLEXIBLE AND PERSONABLE!</div>
<div class="abs hero-text">We are more than happy to help guide your helper in kitchen basics<br>(including hygiene, food storage and shopping on a budget).</div>
<svg class="abs arrow" style="left:51px" viewBox="0 0 48 48"><circle cx="24" cy="24" r="24" fill="#fff" fill-opacity=".45"/><path d="M28 14 L19 24 L28 34" stroke="#fff" stroke-width="4" fill="none"/></svg>
<svg class="abs arrow" style="left:784px" viewBox="0 0 48 48"><circle cx="24" cy="24" r="24" fill="#fff" fill-opacity=".45"/><path d="M20 14 L29 24 L20 34" stroke="#fff" stroke-width="4" fill="none"/></svg>

<h1 class="abs welcome-title">WELCOME TO BRISK LADLES COOKING SCHOOL!</h1>
<p class="abs welcome-text">We are a unique cooking concept where the hands on cooking classes are conducted in your own kitchen! In our cooking lessons we will guide you step by step to help break down the barriers and increase your confidence in the kitchen. As our lessons are conducted in the comfort of your own home we can show you how to work with the equipment and appliances you have. Learn how to cook and prepare heathy meals today!</p>
<a class="abs btn welcome-btn" href="#">KNOW MORE</a>

<div class="abs band"></div>
<div class="abs col" style="left:114px">
  <h2><span>OUR</span> COURSES</h2>
  <div class="shot" role="img" aria-label="Photo of grilled prawns with roasted vegetables" style="background:linear-gradient(135deg,#c9a06a,#e07a45 45%,#b8c46a)"></div>
  <p>Brisk Ladles is all about customising a course that works for you. Before we send you a proposal, we try to find out more about what your family and lifestyle is like. Your answers will help us develop a menu that you can learn and replicate with confidence.</p>
  <a class="btn" href="#">KNOW MORE</a>
</div>
<div class="abs col" style="left:351px">
  <h2><span>OUR</span> TRAINING</h2>
  <div class="shot" role="img" aria-label="Photo of hands stirring vegetables in a frying pan" style="background:linear-gradient(180deg,#e8e4e0,#3a3a3a 55%,#222)"></div>
  <p>All our lessons are hands on and are conducted in your kitchen. If your kitchen is not suitable for our hands on cooking lessons then please contact us to discuss alternative arrangements.</p>
  <a class="btn" href="#">KNOW MORE</a>
</div>
<div class="abs col" style="left:588px">
  <h2><span>OUR</span> PRICING</h2>
  <div class="shot" role="img" aria-label="Photo of a smiling cook giving an approving hand sign" style="background:linear-gradient(135deg,#f2f2f2,#d9b49a 50%,#e8e8e8)"></div>
  <p>Our pricing are quoted in Singapore Dollars and is inclusive of all taxes. Our "Teach Me To Cook" Course fees include all ingredients, recipes in a binder folder and transportation to your home. We will schedule our lessons around your availability!</p>
  <a class="btn" href="#">KNOW MORE</a>
</div>

<section class="abs blog">
  <h2 class="section-h"><span>LATEST</span> BLOG</h2>
  <ul>
    <li>Sneaky Veggies: Korean Spring Onion Pancakes (Pa Jeon)</li>
    <li>Brisk Ladles Kitchen Tip #2 – Sharp Knives</li>
    <li>Saturday Dinner</li>
    <li>Brisk Ladles Kitchen Tip #1 – Ginger Juice</li>
    <li>Tomato Cream Sauce Pasta</li>
  </ul>
</section>
<section class="abs testi">
  <h2 class="section-h">TESTIMONIALS</h2>
  <p><span class="quote">&ldquo;</span> Lorem ipsum dolor sit amet, consetetur sadipscing elitr, sed diam nonumy eirmod tempor invidunt ut labore et dolore magna aliquym erat, sed diam voluptua At vero eos. <span class="quote">&rdquo;</span></p>
  <div class="who">- Dana Rowe</div>
</section>

<div class="abs stripe-pink"></div>
<div class="abs stripe-blue"></div>
<footer class="abs footer"></footer>
<div class="abs copy">&copy;&nbsp; 2014 Briskladles.example</div>
<div class="abs slogan">We are more than happy to discuss food with you!</div>
<div class="abs social"><a href="#">PQ</a><a href="#">Chirply</a><a href="#">Pinboardly</a></div>
</body>
</html>
```